Financial Service Company Need Business Card Design

This is a new startup company, first of its kind to offer this service. We facilitate the movement of deposit funds electronically between home buyers and real estate brokerages.Our customers are DOMIVANS®, real estate brokerages, and home buyers, we identify ourselves as a financial/technology company.
Not looking for anything too flashy. Just a clean design that shows the logo, contact info, etc. Company colors can be seen on attached logo, and 'coming soon page'
www.quorvanta.ca

```html
<!DOCTYPE html>
<html lang="en">
<head>
<meta charset="utf-8">
<title>Quorvanta Business Card</title>
<link href="https://fonts.googleapis.com/css2?family=Exo+2:wght@500;600;700&display=swap" rel="stylesheet">
<style>
  :root{
    --orange:#e9572c;
    --orange-light:#ee633a;
    --slate:#6c6a6b;
    --slate-dark:#5e5c5d;
    --white:#ffffff;
    --backdrop:#ececec;
  }
  *{margin:0;padding:0;box-sizing:border-box}
  html,body{width:1200px;height:1000px;overflow:hidden}
  body{
    background:var(--backdrop);
    font-family:"Exo 2",sans-serif;
    display:flex;flex-direction:column;align-items:center;justify-content:center;gap:60px;
  }
  .card{
    width:600px;height:343px;position:relative;overflow:hidden;
    box-shadow:0 10px 30px rgba(0,0,0,.12);
  }
  /* front */
  .card--front{background:var(--orange-light);display:flex;align-items:center;justify-content:center}
  .card--front .edge{position:absolute;left:0;right:0;bottom:0;height:16px;background:var(--slate)}
  .wordmark{display:flex;align-items:center;gap:16px;color:var(--white);font-weight:600;letter-spacing:.5px}
  .wordmark__square{width:34px;height:34px;background:var(--white)}
  .card--front .wordmark{font-size:58px}
  /* back */
  .card--back{background:var(--slate);color:var(--white)}
  .card--back .band{position:absolute;left:0;right:0;bottom:0;height:18px;background:var(--orange)}
  .card--back .band-top{position:absolute;left:0;top:0;width:100%;height:10px;background:var(--slate-dark)}
  .back__content{position:absolute;left:150px;top:56px}
  .card--back .wordmark{font-size:34px;gap:10px}
  .card--back .wordmark__square{width:20px;height:20px}
  .person{margin:10px 0 0 30px}
  .person__name{font-size:26px;font-weight:700;line-height:1}
  .person__title{font-size:15px;font-weight:600;margin-left:36px}
  .contact{margin:20px 0 0 0;font-size:17px;font-weight:600;line-height:1.45}
  .contact .label{margin-right:10px}
  .contact .gap{margin-left:18px}
  .website{position:absolute;right:40px;bottom:34px;color:var(--orange);font-size:18px;font-weight:700;letter-spacing:1.5px;text-transform:uppercase}
</style>
</head>
<body>
  <section class="card card--front" aria-label="Business card front">
    <div class="wordmark"><span class="wordmark__square"></span><span>Quorvanta</span></div>
    <div class="edge"></div>
  </section>

  <section class="card card--back" aria-label="Business card back">
    <div class="band-top"></div>
    <div class="back__content">
      <div class="wordmark"><span class="wordmark__square"></span><span>Quorvanta</span></div>
      <div class="person">
        <div class="person__name">Alex Morgan</div>
        <div class="person__title">Change</div>
      </div>
      <div class="contact">
        <div>amorgan@quorvanta.ca</div>
        <div><span class="label">Phone</span>555 010 234<span class="gap label">Mobile</span>555 010 234</div>
        <div>48 Harbour Road<span class="gap">Lakeview</span></div>
      </div>
    </div>
    <div class="website">www.quorvanta.ca</div>
    <div class="band"></div>
  </section>
</body>
</html>
```